Images and design ideas provided: Postcard size flier

2 sided postcard size flier to hand people on the street.

A FUN tax business needs a postcard size flier to hand people on the street. Not a typical serious, quiet, office so make the image fun!

Exact wording, logo and key images provided. You are free to add other images as you see fit (such as money).

Side 1: Use image of lady looking up (she should be looking at text provided).All spanish and english text provided. Logo in bottom right corner. Address at bottom of card.

Side 2: Image of lady holding money and pointing. Remove money and have her holding a sign/or some other creative way to have her looking at text. All spanish and english text provided. Logo in bottom right corner. Address at bottom of card.

Size: 4" x 6" horizontal or vertical is ok
Each side can be different and image/design does not have to be related.

Target Market(s)

Age 18-35

Industry/Entity Type

Accounting

Font styles to use
Sans Serif

Colors

Designer to choose colors to be used in the design.

Requirements
Must have
• Use text document provided. All text goes on both sides.
• Should be easy to read from a few feet away.
Nice to have
• Bright colors to attract attention of people walking by to grab flier/card. Images of money ok.
Should not have
• No images of calculators or typical accounting tax forms.

```html
<!DOCTYPE html>
<html lang="en">
<head>
<meta charset="utf-8">
<title>Brightside Tax Co. – Postcard Fliers</title>
<link href="https://fonts.googleapis.com/css2?family=Fira+Sans+Extra+Condensed:wght@700&family=Open+Sans:wght@400;600;700&display=swap" rel="stylesheet">
<style>
  :root{
    --stage:#8c8c8c;
    --bright-red:#d81f3a;
    --deep-red:#c3182b;
    --accent-blue:#2f6fc0;
    --ink:#111111;
    --white:#ffffff;
    --paper:#f3e6d6;
    --flag-pink:#ecc4bf;
    --flag-blue:#b9c9d4;
    --robe-green:#8e9a6a;
  }
  *{margin:0;padding:0;box-sizing:border-box}
  html,body{width:1200px;height:1200px;overflow:hidden}
  body{background:var(--stage);position:relative;font-family:"Open Sans",sans-serif}

  .card{position:absolute;width:549px;height:686px;overflow:hidden;background:var(--paper)}
  .card--front{left:36px;top:39px}
  .card--back{left:617px;top:480px}

  .photo-backdrop{position:absolute;inset:0;
    background:linear-gradient(160deg,var(--paper) 0%,var(--flag-pink) 35%,var(--flag-blue) 55%,var(--flag-pink) 75%,var(--paper) 100%)}
  .photo-person{position:absolute;
    background:linear-gradient(180deg,#d9b27a 0%,#c8302e 18%,#e8c9b0 30%,var(--robe-green) 48%,#7d8a5c 100%);
    border-radius:45% 45% 6px 6px}
  .card--front .photo-person{left:300px;top:230px;width:249px;height:456px}
  .card--back .photo-person{left:129px;top:26px;width:309px;height:480px}

  .wave{position:absolute;left:0;top:0;width:549px;height:686px}

  .headline{position:absolute;left:0;right:0;top:48px;text-align:center;
    font-family:"Fira Sans Extra Condensed",sans-serif;font-weight:700;
    font-size:72px;line-height:1;color:var(--bright-red);letter-spacing:-0.5px}
  .subline{position:absolute;left:0;right:0;top:122px;text-align:center;
    font-family:"Open Sans",sans-serif;font-size:40px;line-height:1;color:var(--ink)}

  .brand{font-family:"Open Sans",sans-serif;font-weight:700;line-height:1;white-space:nowrap}

  .front-contact{position:absolute;left:30px;top:562px;color:var(--white)}
  .front-contact .brand{font-size:26px;color:var(--white)}
  .front-phone{font-family:"Fira Sans Extra Condensed",sans-serif;font-weight:700;
    font-size:44px;line-height:1;margin-top:8px}
  .front-web{font-family:"Open Sans",sans-serif;font-weight:600;font-size:18px;margin-top:4px}

  .back-brand{position:absolute;left:120px;top:526px}
  .back-brand .brand{font-size:30px;color:var(--bright-red)}

  .back-contact{position:absolute;left:68px;top:580px;color:var(--accent-blue);font-size:23px;line-height:1}
  .back-contact li{list-style:none;display:flex;align-items:center;gap:8px;margin-bottom:8px}
  .back-contact svg{width:16px;height:16px;flex:none}
  .back-contact .strong{font-weight:600}
  .back-contact .fax{margin-left:28px;display:flex;align-items:center;gap:8px}
  .back-contact .web{letter-spacing:4px}
</style>
</head>
<body>

<section class="card card--front">
  <div class="photo-backdrop" role="img" aria-label="Faded waving American flag background with falling dollar bills"></div>
  <svg class="wave" viewBox="0 0 549 686" aria-hidden="true">
    <path d="M0,565 C40,495 150,476 270,480 L549,480 L549,686 L0,686Z" fill="var(--deep-red)"/>
    <path d="M0,556 C40,486 150,468 270,472" fill="none" stroke="var(--accent-blue)" stroke-width="7"/>
    <path d="M0,563 C40,493 150,475 270,479" fill="none" stroke="var(--white)" stroke-width="4"/>
  </svg>
  <div class="photo-person" role="img" aria-label="Smiling woman in a costume robe and hat looking up at the headline"></div>

  <h1 class="headline">Get $100 Cash Now!</h1>
  <p class="subline">with paid tax preparation</p>

  <div class="front-contact">
    <div class="brand">Brightside Tax Co.</div>
    <div class="front-phone">(555) 014-2738</div>
    <div class="front-web">www.brightsidetax.com</div>
  </div>
</section>

<section class="card card--back">
  <div class="photo-backdrop" role="img" aria-label="Faded waving American flag background"></div>
  <div class="photo-person" role="img" aria-label="Smiling woman in a costume robe and hat holding a fan of dollar bills"></div>
  <svg class="wave" viewBox="0 0 549 686" aria-hidden="true">
    <path d="M0,562 C60,500 200,482 300,492 C420,502 500,472 549,432 L549,686 L0,686Z" fill="var(--white)"/>
    <path d="M0,554 C60,492 200,474 300,484 C420,494 500,464 549,424" fill="none" stroke="var(--accent-blue)" stroke-width="6"/>
    <path d="M0,562 C60,500 200,482 300,492 C420,502 500,472 549,432" fill="none" stroke="var(--bright-red)" stroke-width="5"/>
  </svg>

  <div class="back-brand">
    <div class="brand">Brightside Tax Co.</div>
  </div>

  <ul class="back-contact">
    <li>
      <svg viewBox="0 0 16 16"><path d="M8 1a5 5 0 0 0-5 5c0 4 5 9 5 9s5-5 5-9a5 5 0 0 0-5-5zm0 7a2 2 0 1 1 0-4 2 2 0 0 1 0 4z" fill="var(--bright-red)"/></svg>
      418 Meadow Ave, Riverton, NY 10000
    </li>
    <li>
      <svg viewBox="0 0 16 16"><path d="M4 1l2.5 3-1.5 2c1 2 3 4 5 5l2-1.5 3 2.5-2 2.5C7 14 2 9 1.5 3.5z" fill="var(--bright-red)"/></svg>
      <span class="strong">(555) 014-2738</span>
      <span class="fax">
        <svg viewBox="0 0 16 16"><path d="M4 1h6l2 2v4H4zM2 7h12v6H2zM4 10h8v5H4z" fill="var(--bright-red)"/></svg>
        <span class="strong">555-014-2790</span>
      </span>
    </li>
    <li>
      <svg viewBox="0 0 16 16"><circle cx="8" cy="8" r="7" fill="none" stroke="var(--bright-red)" stroke-width="2"/><path d="M1 8h14M8 1c3 3 3 11 0 14M8 1c-3 3-3 11 0 14" fill="none" stroke="var(--bright-red)" stroke-width="1.5"/></svg>
      <span class="web">www.brightsidetax.com</span>
    </li>
  </ul>
</section>

</body>
</html>
```